Design a brochure for bulk SMS service provider

I need a brochure design for bulk SMS provder in South Sudan. The company provides API services for SMS, telephony airtime, bulk SMS and other value added SMS services. Our main product allow people and applications to send and receive SMS locally using our software gateway.
We already have the logo design and would like to see the same colors used in the brochure design. I have attached information data to use in the brochure. much of data is in form of lists. I would prefer a grid layout for list items with each having small icon that relates to information the list item communicates.
I have attached a some images of models to use in the design. such as cover page. you can add more images where you see fit.

Target Market(s)

East Africa Region

Industry/Entity Type

Technology, telecommunication, software

Requirements
Must have
• At least 4 brochure pages, all list items properly layout on grids with icons. I will provide icons for out clients section
Nice to have
• More extra images that convey the message well.
Should not have
• Direct copy of brief large text into one section. e.g Don't copy the use cases section verbatim in to page without design and formatting.

```html
<!DOCTYPE html>
<html lang="en">
<head>
<meta charset="utf-8">
<title>kitaSMS brochure</title>
<link rel="stylesheet" href="https://fonts.googleapis.com/css2?family=Lato:ital,wght@0,400;0,700;0,900;1,700&display=swap">
<style>
:root{
  --blue:#1aa6e4;
  --blue-deep:#0d87c4;
  --ink:#1d2430;
  --black:#050505;
  --paper:#ffffff;
  --paper-soft:#eef2f6;
  --grey-line:#5a5f66;
  --stage:#2b2b2b;
}
*{box-sizing:border-box;margin:0;padding:0}
html,body{width:913px;height:1200px;overflow:hidden}
body{background:var(--stage);font-family:"Lato",Arial,sans-serif;color:var(--ink);position:relative}
.spread{position:absolute;left:60px;width:792px;height:560px;display:flex}
.spread--outer{top:25px}
.spread--inner{top:615px}
.page{position:relative;width:396px;height:560px;overflow:hidden}
.abs{position:absolute}

/* back cover */
.back{background:var(--black)}
.brand{display:flex;align-items:center;gap:8px;font-weight:900;letter-spacing:-.3px}
.brand__dot{width:26px;height:26px;border-radius:50%;background:var(--blue);flex:none}
.back .brand{left:150px;top:52px;font-size:27px;color:var(--paper)}
.back__visual{left:95px;top:115px;width:240px;height:255px;border-radius:22px;
  background:linear-gradient(160deg,#4a4d52 0%,#2a2c30 55%,#c9ccd1 100%)}
.wave{left:0;width:100%}
.contact{left:26px;bottom:28px;color:var(--ink)}
.contact__title{font-size:19px;font-weight:900;margin-bottom:5px}
.contact p{font-size:9px;line-height:1.45}

/* front cover */
.front{background:radial-gradient(circle at 30% 25%,#ffffff 0%,#f1f3f6 55%,#e2e6eb 100%)}
.front .brand{left:88px;top:70px;flex-direction:column;align-items:flex-start;gap:8px;font-size:26px;color:var(--ink)}
.front .brand__dot{width:62px;height:62px}
.portrait{left:205px;top:20px;width:190px;height:190px;border-radius:50%;border:7px solid var(--blue);
  background:linear-gradient(150deg,#eceff2 0%,#d7d2cb 45%,#6b4a35 75%,#3b2a20 100%)}
.hands{left:45px;top:300px;width:180px;height:260px;border-radius:18px 18px 0 0;
  background:linear-gradient(170deg,#3a80d8 0%,#7fbf4a 35%,#f2c39b 70%,#e9b48a 100%)}
.tagline{left:248px;top:330px;font-size:22px;font-weight:900;line-height:1.08;color:var(--ink);text-align:left;white-space:nowrap}

/* inner left */
.inside-l{background:var(--paper-soft)}
.about{left:26px;top:18px;width:330px;color:var(--paper)}
.section-title{font-weight:900;font-size:16px;letter-spacing:.2px}
.about p{font-size:7px;line-height:1.5;margin-top:5px}
.features{left:24px;top:140px;width:310px;height:190px;border:1.5px solid var(--blue);padding:18px 10px 0 8px}
.features .section-title{position:absolute;top:-10px;left:20px;background:var(--paper-soft);padding:0 6px;color:var(--ink)}
.feature{display:flex;gap:7px;margin-bottom:4px;font-size:6.6px;line-height:1.35}
.feature__name{width:78px;flex:none;text-align:right;color:var(--blue);text-transform:uppercase;font-weight:700}
.spine-band{left:360px;top:150px;width:36px;height:290px;background:var(--black)}
.solutions{left:22px;top:350px;width:175px}
.solutions .section-title{color:var(--ink);margin-bottom:6px}
.solution{display:flex;gap:6px;font-size:7px;line-height:1.35;margin-bottom:6px}
.solution svg{flex:none;margin-top:1px}
.solution b{font-weight:900}
.network-visual{left:205px;top:360px;width:191px;height:200px;border-radius:60px 0 0 0;
  background:radial-gradient(circle at 45% 45%,#7fd0f5 0%,#1e7fc6 40%,#0b2f6a 100%)}

/* inner right */
.inside-r{background:var(--paper)}
.uses{left:14px;top:40px;width:366px;height:350px;border:1.5px solid var(--grey-line);border-left:none}
.uses-title{left:16px;top:28px;font-size:15px;font-weight:900;color:var(--blue);background:var(--paper);padding-right:8px}
.use{position:absolute;left:0;width:355px}
.use__dot{position:absolute;left:-22px;top:-2px;width:40px;height:40px;border-radius:50%;background:var(--black)}
.use__body{margin-left:30px}
.use__title{font-size:13px;font-weight:900;color:var(--ink)}
.use__text{font-size:6.6px;line-height:1.35;margin-top:2px}
.clients{left:30px;top:410px;width:340px;height:125px;border:1.5px solid var(--blue)}
.clients .section-title{position:absolute;top:-10px;left:50%;transform:translateX(-50%);background:var(--paper);padding:0 8px;color:var(--ink);white-space:nowrap}
.client{position:absolute;display:flex;align-items:center;gap:5px;font-weight:700;color:var(--blue)}
.client__mark{width:14px;height:14px;background:var(--blue-deep);flex:none}
.seal{position:absolute;width:44px;height:44px;border-radius:50%;background:#c9ccd1}
</style>
</head>
<body>

<section class="spread spread--outer">
  <article class="page back">
    <div class="brand abs"><span class="brand__dot"></span>kitaSMS</div>
    <div class="back__visual abs" role="img" aria-label="Illustration of a smartphone surrounded by floating chat and rating message bubbles"></div>
    <svg class="wave abs" style="top:360px" width="396" height="200" viewBox="0 0 396 200">
      <path d="M0 70 C70 20 140 40 200 50 C270 62 330 0 396 10 L396 200 L0 200 Z" fill="var(--blue)"/>
    </svg>
    <div class="contact abs">
      <h2 class="contact__title">Contact us</h2>
      <p>Address : Plot 7, Riverside Office Park, Suite 12, Juba – South Sudan</p>
      <p>Email: Sales: sales@kitasms-example.com Support: hello@kitasms-example.com</p>
      <p>Telephone: +211 900 000 123</p>
    </div>
  </article>

  <article class="page front">
    <div class="brand abs"><span class="brand__dot"></span>kitaSMS</div>
    <div class="portrait abs" role="img" aria-label="Photo of a smiling young woman reading a text message on her phone"></div>
    <svg class="wave abs" style="top:200px" width="396" height="360" viewBox="0 0 396 360">
      <path d="M250 10 L290 0 L275 30 Z" fill="var(--blue)"/>
      <path d="M150 140 C220 60 320 90 396 70 L396 360 L230 360 C260 300 230 240 150 140 Z" fill="var(--blue)"/>
      <path d="M215 132 L240 122 L229 146 Z" fill="#4caf3c"/>
      <path d="M8 100 L34 92 L23 118 Z" fill="#3a8fe0"/>
    </svg>
    <div class="hands abs" role="img" aria-label="Illustration of two hands holding a smartphone with green and blue message bubbles"></div>
    <h1 class="tagline abs">Bulk SMS<br>&nbsp;&nbsp;Service<br>&nbsp;&nbsp;&nbsp;Provider</h1>
  </article>
</section>

<section class="spread spread--inner">
  <article class="page inside-l">
    <svg class="abs" style="top:0;left:0" width="396" height="180" viewBox="0 0 396 180">
      <path d="M0 0 L396 0 L396 160 C300 110 150 110 0 125 Z" fill="var(--blue)"/>
    </svg>
    <div class="about abs">
      <h2 class="section-title">ABOUT US</h2>
      <p>KitaSMS is a bulk SMS provider in South Sudan with over five years of experience in multi-route messaging. We help businesses grow sales and customer satisfaction through campaigns, instant alerts, OTPs, notifications and two-way conversations.</p>
      <p>Our focus is reliable routing and delivery, working with partner telecom networks so every message reaches its destination on time.</p>
    </div>
    <div class="spine-band abs"></div>
    <div class="features abs">
      <h2 class="section-title">OUR FEATURES</h2>
      <div class="feature"><span class="feature__name">Send SMS</span><span>Send SMS in minutes through web, HTTP or SMPP.</span></div>
      <div class="feature"><span class="feature__name">Receive SMS</span><span>Receive SMS using keywords, short codes and long codes.</span></div>
      <div class="feature"><span class="feature__name">Auto responders</span><span>Compose an automated reply sent to every customer who texts your short code.</span></div>
      <div class="feature"><span class="feature__name">Two way SMS</span><span>Request short or long codes to chat with customers in both directions.</span></div>
      <div class="feature"><span class="feature__name">SMS polls</span><span>Run polls, engage customers and build your contact database.</span></div>
      <div class="feature"><span class="feature__name">Airtime</span><span>Send airtime to customers on any network with one simple API call.</span></div>
      <div class="feature"><span class="feature__name">Delivery reports</span><span>See the status of every outgoing message at any time.</span></div>
      <div class="feature"><span class="feature__name">USSD</span><span>Build interactive applications on top of the USSD framework.</span></div>
    </div>
    <div class="solutions abs">
      <h2 class="section-title">OUR SOLUTIONS</h2>
      <div class="solution"><svg width="9" height="9" viewBox="0 0 10 10"><circle cx="5" cy="5" r="4.3" fill="none" stroke="var(--ink)" stroke-width="1"/><path d="M3 5.2 L4.5 6.6 L7.2 3.6" fill="none" stroke="var(--ink)" stroke-width="1.1"/></svg><span><b>SMS aggregation</b> – Send and receive SMS easily from any network in South Sudan</span></div>
      <div class="solution"><svg width="9" height="9" viewBox="0 0 10 10"><circle cx="5" cy="5" r="4.3" fill="none" stroke="var(--ink)" stroke-width="1"/><path d="M3 5.2 L4.5 6.6 L7.2 3.6" fill="none" stroke="var(--ink)" stroke-width="1.1"/></svg><span><b>Bulk SMS</b> – Send to multiple people at the same time using one request</span></div>
      <div class="solution"><svg width="9" height="9" viewBox="0 0 10 10"><circle cx="5" cy="5" r="4.3" fill="none" stroke="var(--ink)" stroke-width="1"/><path d="M3 5.2 L4.5 6.6 L7.2 3.6" fill="none" stroke="var(--ink)" stroke-width="1.1"/></svg><span><b>Airtime</b> – Provide airtime distribution services to mobile phone users in South Sudan</span></div>
      <div class="solution"><svg width="9" height="9" viewBox="0 0 10 10"><circle cx="5" cy="5" r="4.3" fill="none" stroke="var(--ink)" stroke-width="1"/><path d="M3 5.2 L4.5 6.6 L7.2 3.6" fill="none" stroke="var(--ink)" stroke-width="1.1"/></svg><span><b>USSD</b> – Build interactive applications using our USSD API</span></div>
      <div class="solution"><svg width="9" height="9" viewBox="0 0 10 10"><circle cx="5" cy="5" r="4.3" fill="none" stroke="var(--ink)" stroke-width="1"/><path d="M3 5.2 L4.5 6.6 L7.2 3.6" fill="none" stroke="var(--ink)" stroke-width="1.1"/></svg><span><b>Short codes</b> – Offer short numbers to send and receive SMS in South Sudan</span></div>
    </div>
    <div class="network-visual abs" role="img" aria-label="Photo of a finger touching a glowing envelope icon over a world map with message icons"></div>
  </article>

  <article class="page inside-r">
    <svg class="abs" style="top:0;left:0" width="120" height="130" viewBox="0 0 120 130">
      <path d="M0 0 L110 0 C60 20 20 60 0 130 Z" fill="var(--blue)"/>
    </svg>
    <div class="uses abs">
      <div class="use" style="top:22px"><span class="use__dot"></span><div class="use__body"><h3 class="use__title">Marketing and Ads</h3><p class="use__text">Send promotional messages in bulk, personalize texts, share offers and reach thousands of customers with one campaign.</p></div></div>
      <div class="use" style="top:76px"><span class="use__dot"></span><div class="use__body"><h3 class="use__title">Banking and Financial services</h3><p class="use__text">Send transaction alerts, balance updates and one-time passwords through a secure and reliable queue.</p></div></div>
      <div class="use" style="top:130px"><span class="use__dot"></span><div class="use__body"><h3 class="use__title">NGO</h3><p class="use__text">Reach communities with updates and alerts, run SMS surveys and keep field teams informed in real time.</p></div></div>
      <div class="use" style="top:184px"><span class="use__dot"></span><div class="use__body"><h3 class="use__title">Healthcare</h3><p class="use__text">Send appointment reminders, share test results and let patients request help with a simple text message.</p></div></div>
      <div class="use" style="top:238px"><span class="use__dot"></span><div class="use__body"><h3 class="use__title">Restaurant and takeways</h3><p class="use__text">Share offers and discount vouchers, take orders by text and grow your loyal customer base.</p></div></div>
      <div class="use" style="top:292px"><span class="use__dot"></span><div class="use__body"><h3 class="use__title">Education</h3><p class="use__text">Send exam schedules and results, share reading material and collect quick feedback from students and parents.</p></div></div>
    </div>
    <h2 class="uses-title abs">USE CASES</h2>
    <div class="clients abs">
      <h2 class="section-title">OUR CLIENTS</h2>
      <span class="client" style="left:18px;top:22px;font-size:22px">Hopewell Aid</span>
      <span class="seal" style="left:170px;top:24px"></span>
      <span class="client" style="left:232px;top:32px;font-size:17px;color:var(--ink)">PulseSurvey</span>
      <span class="client" style="left:24px;top:78px;font-size:12px"><span class="client__mark"></span>Beacon Trust</span>
      <span class="client" style="left:140px;top:82px;font-size:13px">Clearview Health</span>
    </div>
  </article>
</section>

</body>
</html>
```